Professional consulting firm needing a Word document template

I need a Word document template that can be used flexibly for a flyer or brochure of 1 to 3 pages in length. The first page should be designed in a way that it can stand alone as a one-page flyer without a formal cover page. I have attached sample text as a Word document that could be used as the basis for the first 1-2 pages, however I do need three page layouts designed to give flexibility to use as a 3 page booklet. I have attached our brand guidelines, logo, and some stock images that I have previously purchased (they may not all be useful but it gives some options). <br/>The Word document needs to be set up in away that it can easily be edited to accommodate updates to the text, and some variation in the quantity of text on each page. Each page should be able to accommodate a mixture of paragraph text, bullet points, small boxes to call out highlights, one or more images, and some white space to avoid clutter. It should look professional yet engaging and modern.

Font styles to use
Sans Serif

Requirements
Must have
• Must be an editable Microsoft Word document, using the text provided. Must be a layout suitable to use as 1 page, up to 3 pages. Must comply with brand guidelines.

```html
<!DOCTYPE html>
<html lang="en">
<head>
<meta charset="utf-8">
<title>Train Driver Competency Indicator Development Project – Trifold Brochure</title>
<link href="https://fonts.googleapis.com/css2?family=Open+Sans:wght@400;600;700&display=swap" rel="stylesheet">
<style>
  :root {
    --navy: #0e2232;
    --blue: #29abe2;
    --blue-light: #4cc0ee;
    --blue-mid: #1c8fcf;
    --photo-top: #a9dcee;
    --photo-bottom: #e3f4f9;
    --teal-pale: #cfeeee;
    --paper: #ffffff;
    --paper-grey: #f1f3f4;
    --ink: #1f2a33;
    --rule-dark: #5a6d7c;
    --stage: #e8edef;
  }
  * { box-sizing: border-box; margin: 0; padding: 0; }
  html, body { width: 1200px; height: 800px; overflow: hidden; }
  body {
    background: var(--stage);
    font-family: "Open Sans", Arial, sans-serif;
    color: var(--ink);
    position: relative;
  }
  .sheet {
    position: absolute;
    top: 170px;
    width: 570px;
    height: 440px;
    display: flex;
    box-shadow: 0 6px 18px rgba(0,0,0,.18);
  }
  .sheet--outside { left: 20px; }
  .sheet--inside { left: 610px; }
  .panel {
    position: relative;
    width: 190px;
    height: 100%;
    overflow: hidden;
    font-size: 6.4px;
    line-height: 1.4;
  }
  .panel + .panel { border-left: 1px solid rgba(0,0,0,.08); }
  .panel--dark { background: var(--navy); color: var(--paper); }
  .panel--white { background: var(--paper); }
  .panel--grey { background: var(--paper-grey); }
  .panel--blue { background: var(--blue-mid); color: var(--paper); }
  p { margin-bottom: 6px; }
  .heading { font-weight: 700; font-size: 9px; line-height: 1.2; }
  .dot-cluster { position: absolute; border-radius: 50%; }
  .dot-cluster--light { background: var(--paper); opacity: .9; }
  .dot-cluster--pale { background: var(--teal-pale); }
  .photo { background: linear-gradient(180deg, var(--photo-top) 0%, var(--photo-bottom) 100%); }

  /* Outside – competencies */
  .competencies .heading { position: absolute; left: 14px; top: 34px; font-size: 10px; }
  .callout {
    position: absolute;
    left: 10px; top: 58px; width: 170px;
    background: var(--blue);
    padding: 10px 9px;
    border: 1px solid var(--paper);
    outline: 3px solid var(--blue);
  }
  .competencies .body-text { position: absolute; left: 14px; top: 170px; width: 162px; }
  .competencies .rule { position: absolute; left: 0; right: 0; top: 345px; border-top: 1px solid var(--rule-dark); }

  /* Outside – involvement */
  .involved .heading { position: absolute; left: 14px; top: 34px; width: 162px; text-align: center; }
  .involved .body-text { position: absolute; left: 14px; top: 58px; width: 162px; }
  .band { position: absolute; left: 0; right: 0; bottom: 0; height: 98px; background: var(--blue); }
  .band--tab { position: absolute; left: 0; bottom: 0; width: 28px; height: 98px; background: var(--blue-light); }
  .contact {
    position: absolute; left: 0; right: 0; bottom: 30px;
    text-align: center; color: var(--navy); font-size: 6.6px; line-height: 1.5;
  }

  /* Outside – cover */
  .brand { position: absolute; left: 20px; top: 38px; display: flex; align-items: center; gap: 6px; }
  .brand__mark { width: 12px; height: 12px; border-radius: 50%; background: var(--blue); }
  .brand__name { font-size: 22px; font-weight: 700; color: var(--navy); letter-spacing: 1px; }
  .cover .photo { position: absolute; left: 18px; top: 92px; width: 154px; height: 210px; }
  .cover .frame { position: absolute; left: 12px; top: 86px; width: 166px; height: 260px; border: 1px solid var(--navy); }
  .cover svg { position: absolute; left: 0; bottom: 0; }

  /* Inside – intro */
  .title-box {
    position: absolute; left: 14px; top: 18px; width: 162px;
    border: 1px solid var(--navy); background: var(--paper);
    padding: 5px; text-align: center; font-weight: 700; font-size: 7.6px; line-height: 1.25;
  }
  .intro .photo { position: absolute; left: 0; top: 52px; width: 190px; height: 120px; }
  .intro .lead { position: absolute; left: 14px; top: 186px; width: 166px; font-size: 6.8px; }
  .list-frame {
    position: absolute; left: 14px; top: 262px; width: 162px; height: 136px;
    border: 1px solid var(--navy); padding: 8px 8px 8px 10px;
  }
  .competency-list { list-style: none; font-size: 6.6px; line-height: 1.45; }
  .competency-list li::before { content: "•"; color: var(--blue); margin-right: 6px; }

  /* Inside – benefits */
  .benefits .heading { position: absolute; left: 14px; top: 22px; width: 162px; text-align: center; }
  .benefits .underline { position: absolute; left: 20px; right: 20px; top: 46px; border-top: 1px solid rgba(255,255,255,.6); }
  .benefits .body-text { position: absolute; left: 14px; top: 54px; width: 162px; }
  .benefits .photo { position: absolute; left: 12px; top: 160px; width: 166px; height: 220px; border: 2px solid var(--paper); }

  /* Inside – activities */
  .activities .topbar { position: absolute; left: 0; right: 0; top: 0; height: 26px; background: var(--teal-pale); }
  .activities .heading { position: absolute; left: 14px; top: 32px; font-size: 8.6px; }
  .activities .body-text { position: absolute; left: 14px; top: 50px; width: 164px; }
  .activity-list { padding-left: 9px; }
  .activity-list li { margin-bottom: 5px; }
  .activity-list strong { font-weight: 700; }
</style>
</head>
<body>

<section class="sheet sheet--outside" aria-label="Brochure outside">
  <div class="panel panel--dark competencies">
    <div class="dot-cluster dot-cluster--light" role="img" aria-label="Decorative dot circle" style="left:-22px;top:-10px;width:56px;height:56px;"></div>
    <h2 class="heading">Underlying competencies:</h2>
    <div class="callout">The underpinning knowledge and skills required by a train driver, to perform a range of different tasks effectively. Underlying competencies include both ‘technical’ and ‘non-technical’ skills. They are not specific to one driving task, but help build resilient performance across all tasks, conditions or situations that a driver may encounter.</div>
    <div class="body-text">In contrast to other performance marker systems, the current project aims to include both ‘technical’ and ‘non-technical’ skills in an integrated framework, with substantial input from drivers across the industry, both in passenger and freight operations. The aim is to develop a framework that uses a language that describes performance in a way that is relatable to drivers, trainers, and assessors.</div>
    <div class="rule"></div>
    <div class="dot-cluster dot-cluster--light" role="img" aria-label="Decorative dot circle" style="left:10px;bottom:-20px;width:70px;height:70px;"></div>
  </div>

  <div class="panel panel--dark involved">
    <h2 class="heading">What is involved?</h2>
    <div class="body-text">
      <p>It is anticipated that workshops will be run in Brisbane, Sydney and Melbourne. We would appreciate support from participating organisations in providing a workshop venue where possible. Apart from the in-kind support of providing access to personnel and a meeting room, there is no cost associated with participation in the project.</p>
      <p>In addition to the activities involving industry participation, we will also be completing a detailed task analysis and analysing incident reports and other publicly available data, to help inform the development of the framework.</p>
      <p>We look forward to hearing from organisations interested in being part of this landmark project.</p>
    </div>
    <div class="band"></div>
    <div class="band--tab"></div>
    <div class="contact">Company Name<br>www.website.com.au<br>contact@website.com.au</div>
  </div>

  <div class="panel panel--white cover">
    <div class="brand"><span class="brand__mark"></span><span class="brand__name">Veridan</span></div>
    <div class="frame"></div>
    <div class="photo" role="img" aria-label="Photo of a train passing through a bright station"></div>
    <svg width="190" height="110" viewBox="0 0 190 110" aria-hidden="true">
      <path d="M0 40 Q95 10 190 30 L190 110 L0 110 Z" fill="#29abe2"/>
      <path d="M0 40 Q95 10 190 30" fill="none" stroke="#ffffff" stroke-width="2"/>
    </svg>
    <div class="dot-cluster dot-cluster--light" role="img" aria-label="Decorative dot circle" style="right:-10px;bottom:4px;width:54px;height:54px;"></div>
  </div>
</section>

<section class="sheet sheet--inside" aria-label="Brochure inside">
  <div class="panel panel--white intro">
    <div class="photo" role="img" aria-label="Photo of a train passing through a bright station"></div>
    <h1 class="title-box">Train Driver Competency Indicator Development Project</h1>
    <p class="lead">We are commencing an applied research project to develop and test a framework of underlying core competencies for train driver performance. The objective of the project is to identify observable indicators that describe effective performance in the following types of underlying competencies:</p>
    <div class="list-frame">
      <ul class="competency-list">
        <li>Application of Procedures</li>
        <li>Communication</li>
        <li>Operation of Tools / Equipment</li>
        <li>Problem Solving and Decision Making</li>
        <li>Route Knowledge</li>
        <li>Self Management</li>
        <li>Situation Awareness</li>
        <li>System Knowledge</li>
        <li>Teamwork and Leadership</li>
        <li>Train Handling</li>
        <li>Workload Management</li>
      </ul>
    </div>
    <div class="dot-cluster dot-cluster--pale" role="img" aria-label="Decorative dot circle" style="left:-20px;bottom:-14px;width:60px;height:60px;"></div>
  </div>

  <div class="panel panel--blue benefits">
    <h2 class="heading">What are the benefits for participating organisations?</h2>
    <div class="underline"></div>
    <div class="body-text">All participating rail organisations will receive a copy of the performance indicator framework, which they are free to use or adapt for application within their own operation. A summary report will also be provided, outlining the methodology and aggregated results of the data collection activities. All results will be presented in a de-identified way, to ensure the anonymity of participating organisations and individuals.</div>
    <div class="photo" role="img" aria-label="Photo of a train passing through a bright station"></div>
  </div>

  <div class="panel panel--grey activities">
    <div class="topbar"></div>
    <h2 class="heading">What is involved?</h2>
    <div class="body-text">
      <p>Participating organisations will be invited to provide in-kind support for the following activities during the period April – June 2020:</p>
      <ul class="activity-list">
        <li><strong>Interviews with volunteer Driver participants:</strong> individual discussions with our researchers about drivers’ previous experiences, to gather information about expert driving strategies and positive techniques used in normal and abnormal operations.</li>
        <li><strong>Initial workshop:</strong> a facilitated group workshop to understand the links between underlying competencies and driving tasks, and to understand drivers’ perceptions of what each underlying competency looks like in practice.</li>
        <li><strong>Driver Training Survey:</strong> a voluntary survey will be distributed, requesting Driver Trainers’ and Assessors’ views on the importance of underlying competencies in driving performance, and further data about expert strategies and techniques.</li>
        <li><strong>Follow-up workshop:</strong> a facilitated group workshop to test and refine the performance indicators. Where possible, indicators will be tested through participants providing ratings of a video sample of actual performance, to determine whether multiple raters can distinguish between competency categories.</li>
      </ul>
    </div>
    <div class="dot-cluster dot-cluster--pale" role="img" aria-label="Decorative dot circle" style="right:-16px;bottom:40px;width:60px;height:60px;"></div>
  </div>
</section>

</body>
</html>
```